Label For Hand soap

Hello,

I would like to get your assistance with creating a label for my hand soap that I am in the process of developing. I would like the label to look simple visually appealing and eye catching similar to a cologne bottle's label. I would like there to be graphic or illustration accompanied with the text. The color scheme is black. I would like the background of the label to be transparent so that I can show the color of my product. I have attached some pictures of my bottle and some labels that I like for your reference. The name of my brand is Velor. The hand soap scent is candied pineapples.

Thanks

```html
<!DOCTYPE html>
<html lang="en">
<head>
<meta charset="utf-8">
<title>Velor Hand Soap Label</title>
<link rel="stylesheet" href="https://fonts.googleapis.com/css2?family=Playfair+Display:wght@500;700&display=swap">
<style>
  :root {
    --soap: #8e8552;
    --soap-light: #a39a66;
    --ink: #141210;
    --ink-soft: rgba(20, 18, 16, 0.55);
    --paper-text: #f1ecd9;
  }
  html, body {
    margin: 0;
    padding: 0;
    width: 1200px;
    height: 1200px;
    overflow: hidden;
    background: var(--soap);
  }
  .canvas {
    position: relative;
    width: 1200px;
    height: 1200px;
    background: radial-gradient(circle at 50% 40%, var(--soap-light), var(--soap) 70%);
  }
  .label-art {
    position: absolute;
    left: 0;
    top: 0;
  }
  .brand-name {
    font-family: "Playfair Display", serif;
    font-weight: 500;
    font-size: 104px;
    letter-spacing: 2px;
    fill: var(--ink);
  }
  .product-title {
    font-family: "Playfair Display", serif;
    font-weight: 500;
    font-size: 150px;
    fill: var(--ink);
  }
  .scent-name {
    font-family: "Playfair Display", serif;
    font-weight: 700;
    font-size: 27px;
    letter-spacing: 0.5px;
    fill: var(--paper-text);
  }
  .volume {
    font-family: "Playfair Display", serif;
    font-weight: 500;
    font-size: 22px;
    letter-spacing: 2px;
    fill: var(--ink);
  }
</style>
</head>
<body>
<div class="canvas">
  <svg class="label-art" width="1200" height="1200" viewBox="0 0 1200 1200" xmlns="http://www.w3.org/2000/svg">
    <g class="label-frame" fill="none" stroke="var(--ink)">
      <rect x="210" y="75" width="780" height="1053" stroke-width="3"/>
      <rect x="222" y="87" width="756" height="1029" stroke-width="1.5"/>
      <rect x="248" y="113" width="704" height="977" stroke-width="1.5"/>
      <rect x="256" y="121" width="688" height="961" stroke-width="3"/>
    </g>
    <path class="frame-band" role="img" aria-label="Fine key-pattern border band"
          fill="var(--ink-soft)" fill-rule="evenodd"
          d="M225 90 H975 V1113 H225 Z M245 110 V1093 H955 V110 Z"/>

    <g class="corner-flourish" fill="var(--ink-soft)">
      <rect role="img" aria-label="Ornamental corner flourish" x="272" y="137" width="105" height="190" rx="40"/>
      <rect role="img" aria-label="Ornamental corner flourish" x="823" y="137" width="105" height="190" rx="40"/>
      <path role="img" aria-label="Ornamental corner flourish"
            d="M266 876 Q266 866 276 866 H288 Q298 866 298 876 V1030 H380 Q392 1030 392 1042 V1054 Q392 1068 380 1068 H278 Q266 1068 266 1056 Z"/>
      <path role="img" aria-label="Ornamental corner flourish"
            d="M934 876 Q934 866 924 866 H912 Q902 866 902 876 V1030 H820 Q808 1030 808 1042 V1054 Q808 1068 820 1068 H922 Q934 1068 934 1056 Z"/>
    </g>

    <text class="brand-name" x="600" y="283" text-anchor="middle">Velor</text>

    <g class="title-plate" fill="none" stroke="var(--ink)">
      <rect x="299" y="427" width="586" height="378" rx="42" stroke-width="3"/>
      <rect x="321" y="449" width="542" height="334" rx="30" stroke-width="1.5"/>
    </g>
    <path class="title-plate-band" role="img" aria-label="Beaded pattern border of the title plate"
          fill="var(--ink-soft)" fill-rule="evenodd"
          d="M345 432 H839 A41 41 0 0 1 880 473 V759 A41 41 0 0 1 839 800 H345 A41 41 0 0 1 304 759 V473 A41 41 0 0 1 345 432 Z
             M348 446 A28 28 0 0 0 320 474 V758 A28 28 0 0 0 348 786 H836 A28 28 0 0 0 864 758 V474 A28 28 0 0 0 836 446 Z"/>
    <text class="product-title" x="600" y="612" text-anchor="middle">HAND</text>
    <text class="product-title" x="600" y="758" text-anchor="middle">SOAP</text>

    <g class="scent-banner">
      <path d="M311 932 L350 880 L380 900 H820 L850 880 L889 932 L850 984 L820 964 H380 L350 984 Z"
            fill="none" stroke="var(--ink)" stroke-width="3"/>
      <path d="M330 932 L356 898 L382 914 H818 L844 898 L870 932 L844 966 L818 950 H382 L356 966 Z"
            fill="none" stroke="var(--ink)" stroke-width="1.5"/>
      <rect x="392" y="912" width="416" height="42" rx="21" fill="var(--ink)"/>
      <text class="scent-name" x="600" y="943" text-anchor="middle">CANDIED PINEAPPLES.</text>
    </g>

    <text class="volume" x="600" y="1062" text-anchor="middle">8 FL.OZ.</text>
  </svg>
</div>
</body>
</html>
```